nukh almasira
nukh almasira - Corporate Services
Creative Brief
Simple
Kadhim Rubaie كاظم الربيعي
CEO المدير المفوض
Locality 482 - Alley 17 - House 8 Al Mansour - Baghdad - Iraq محلة 482 - زقاق 17 - دار 8 المنصور - بغداد - العراق
CEO@nukhalmasira.example
www.nukhalmasira.example
Concepts
Business Cards and Stationery for new compliance company.
Business Cards and Stationery for Background Check Company
qorvel42 qorvel42
good design but i hope you use the same name and information in the brief and if you can work on the logo cause i want to add the Arabic name of the company ( نخبة المسيرة ) if you can put the logo in the left and the name of the company in English and Arabic in the right of the logo and use the same font and size in Arabic and English name
Brisk Brisk
Ok
Please show me the whole stationary not only the business card
please use this e-mail on the letterhead only info@nukhalmasira.example and the address in arabic language use it only in the letterhead too thankyou

```html
<!DOCTYPE html>
<html lang="en">
<head>
<meta charset="UTF-8">
<title>nukh almasira – Business Card</title>
<link href="https://fonts.googleapis.com/css2?family=Montserrat:wght@400;500&display=swap" rel="stylesheet">
<style>
  :root {
    --canvas-bg: #e9eaec;
    --card-bg: #ffffff;
    --brand-blue: #1f8bd0;
    --deep-blue: #1671b3;
    --brand-orange: #f6a623;
    --silver: #cfd6dd;
    --ink: #3a3f46;
    --on-blue: #ffffff;
  }
  * { margin: 0; padding: 0; box-sizing: border-box; }
  html, body {
    width: 1200px; height: 768px; overflow: hidden;
    background: var(--canvas-bg);
    font-family: "Montserrat", Arial, sans-serif;
  }
  .business-card {
    position: absolute; left: 120px; top: 98px;
    width: 960px; height: 572px;
    background: var(--card-bg);
    overflow: hidden;
    box-shadow: 0 18px 40px rgba(0,0,0,0.18);
  }
  .accent-band {
    position: absolute; left: 0; right: 0; top: 360px; bottom: 0;
    background: linear-gradient(180deg,
      var(--brand-orange) 0%,
      var(--silver) 16%,
      var(--brand-blue) 34%,
      var(--deep-blue) 100%);
  }
  .brand {
    position: absolute; left: 40px; top: 190px;
    display: flex; align-items: center; gap: 16px;
  }
  .brand-dot {
    width: 30px; height: 30px; border-radius: 50%;
    background: var(--brand-orange);
  }
  .brand-name {
    font-weight: 500; font-size: 36px; letter-spacing: 2px;
    text-transform: uppercase; color: var(--brand-blue);
  }
  .holder { position: absolute; right: 25px; top: 62px; text-align: right; }
  .holder-name {
    font-weight: 500; font-size: 31px; letter-spacing: 2px;
    color: var(--brand-blue); text-transform: uppercase;
  }
  .holder-title {
    margin-top: 6px;
    font-weight: 500; font-size: 20px; letter-spacing: 2px;
    color: var(--ink); text-transform: uppercase;
  }
  .address {
    position: absolute; right: 25px; top: 286px; text-align: right;
    font-size: 15px; line-height: 30px; color: var(--ink);
  }
  .contact-list {
    position: absolute; right: 25px; top: 392px;
    list-style: none;
  }
  .contact-list li {
    display: flex; justify-content: flex-end; align-items: center; gap: 14px;
    height: 34px; font-size: 14px; color: var(--on-blue);
  }
  .contact-list svg { width: 16px; height: 16px; flex: none; }
</style>
</head>
<body>
  <div class="business-card">
    <div class="accent-band" role="img" aria-label="Flowing accent band in orange, silver and blue"></div>

    <div class="brand">
      <span class="brand-dot"></span>
      <span class="brand-name">nukh almasira</span>
    </div>

    <div class="holder">
      <p class="holder-name">Tobin Hallard</p>
      <p class="holder-title">President</p>
    </div>

    <div class="address">
      <p>77 Harbor Walk North</p>
      <p>Linden Park NW 4</p>
    </div>

    <ul class="contact-list">
      <li>012 555 0142
        <svg viewBox="0 0 16 16"><path d="M3 1.5 L6 1.5 L7 5 L5.2 6.3 C6 8.2 7.8 10 9.7 10.8 L11 9 L14.5 10 L14.5 13 C14.5 14 13.6 14.6 12.6 14.5 C6.8 13.8 2.2 9.2 1.5 3.4 C1.4 2.4 2 1.5 3 1.5 Z" fill="#fff"/></svg>
      </li>
      <li>012 555 0178
        <svg viewBox="0 0 16 16"><rect x="4" y="1" width="8" height="14" rx="1.5" fill="#fff"/><rect x="5.5" y="3" width="5" height="8" fill="var(--brand-blue)"/></svg>
      </li>
      <li>012 555 0193
        <svg viewBox="0 0 16 16"><rect x="2" y="6" width="12" height="8" rx="1" fill="#fff"/><rect x="4.5" y="1.5" width="7" height="5" fill="#fff"/></svg>
      </li>
      <li>tobin@nukhalmasira.example
        <svg viewBox="0 0 16 16"><rect x="1" y="3.5" width="14" height="9" rx="1" fill="#fff"/><path d="M1.5 4 L8 9 L14.5 4" fill="none" stroke="var(--brand-blue)" stroke-width="1.3"/></svg>
      </li>
      <li>www.nukhalmasira.example
        <svg viewBox="0 0 16 16"><circle cx="8" cy="8" r="6.5" fill="none" stroke="#fff" stroke-width="1.5"/><path d="M1.5 8 H14.5 M8 1.5 C5 5 5 11 8 14.5 M8 1.5 C11 5 11 11 8 14.5" fill="none" stroke="#fff" stroke-width="1.1"/></svg>
      </li>
    </ul>
  </div>
</body>
</html>
```